Clean professional design needed for landscape property business

We need a logo for a new lawncare, landscaping , property maintenance business called Fernway Grove.
Our services include lawn mowing, garden maintenance, clean ups and some property maintenance.
We want a double sided business card that is clean and very professional using the colour scheme from our logo which is provided.
the business card should have impact as we will use these to drop into people's letterboxes as a marketing drop.
Initially we want to see what you come up with so there is a very wide scope here to work with.

Project Deadline Extended
Reason: we feel our original deadline was too short. we have extended to give more time for quality submissions.

Target Market(s)

High end property owners who don't wish to do there own gardneing or property maintenance

Industry/Entity Type

Business

Contact Information for Business Card

Name
Postion/ Title
Phone number
mobile
web address
physical address

services offered

Font styles to use
Sans Serif

Requirements
Must have
• curved edges preferrred
Nice to have
• We like the idea of the logo being embossed or etched into the card so it looks like it is below the surface of the card
Should not have
• No stock images or characters.

```html
<!DOCTYPE html>
<html lang="en">
<head>
<meta charset="utf-8">
<title>Fernway Grove – Business Card</title>
<link rel="stylesheet" href="https://fonts.googleapis.com/css2?family=Roboto:wght@400;500;700&display=swap">
<style>
  :root {
    --backdrop: #3a3a3a;
    --card: #1f1f1f;
    --green: #7cc418;
    --white: #f2f2f2;
    --muted: #d6d6d6;
  }
  * { margin: 0; padding: 0; box-sizing: border-box; }
  html, body {
    width: 1200px; height: 900px; overflow: hidden;
    background: var(--backdrop);
    font-family: "Roboto", Arial, sans-serif;
  }
  .stage {
    position: relative; width: 1200px; height: 900px;
    display: flex; align-items: center; justify-content: center; gap: 40px;
  }
  .card {
    position: relative; width: 525px; height: 300px;
    background: var(--card); border-radius: 24px; overflow: hidden;
  }
  .brand {
    display: flex; align-items: center; gap: 8px;
    color: var(--green); font-weight: 700; letter-spacing: -0.5px;
  }
  .brand-dot { width: 0.5em; height: 0.5em; border-radius: 50%; background: var(--green); }

  /* Front */
  .card-front .brand { position: absolute; top: 38px; right: 34px; font-size: 26px; }
  .card-front .divider {
    position: absolute; left: 34px; right: 34px; top: 148px;
    height: 1.5px; background: var(--green);
  }
  .online {
    position: absolute; top: 162px; right: 34px;
    list-style: none; text-align: right; font-size: 13px; color: var(--white);
  }
  .online li { display: flex; align-items: center; justify-content: flex-end; gap: 8px; margin-bottom: 6px; }
  .person { position: absolute; left: 34px; top: 196px; }
  .person-name { color: var(--green); font-size: 19px; font-weight: 500; }
  .person-title { color: var(--white); font-size: 15px; margin-top: 2px; }
  .phones { position: absolute; left: 34px; bottom: 24px; list-style: none; font-size: 16px; color: var(--white); }
  .phones li { display: flex; align-items: center; gap: 12px; margin-top: 4px; }
  .icon { width: 14px; height: 14px; fill: var(--green); flex: none; }

  /* Back */
  .card-back .brand-block {
    position: absolute; right: 60px; top: 110px; text-align: right;
  }
  .card-back .brand { font-size: 40px; justify-content: flex-end; }
  .services { margin-top: 10px; color: var(--muted); font-size: 12.5px; line-height: 1.4; }
  .services .sep { color: var(--green); }
</style>
</head>
<body>
<main class="stage">
  <section class="card card-front" aria-label="Business card front">
    <div class="brand"><span>Fernway Grove</span><span class="brand-dot"></span></div>
    <div class="divider"></div>
    <ul class="online">
      <li>alex@fernwaygrove.com
        <svg class="icon" viewBox="0 0 16 16"><path d="M1 3h14v10H1z M1 3l7 6 7-6" fill="var(--green)" stroke="var(--card)" stroke-width="1.2"/></svg></li>
      <li>www.fernwaygrove.com
        <svg class="icon" viewBox="0 0 16 16"><circle cx="8" cy="8" r="7"/><path d="M1 8h14M8 1c3 3 3 11 0 14M8 1c-3 3-3 11 0 14" stroke="var(--card)" stroke-width="1.2" fill="none"/></svg></li>
    </ul>
    <div class="person">
      <p class="person-name">Alex Morgan</p>
      <p class="person-title">President</p>
    </div>
    <ul class="phones">
      <li><svg class="icon" viewBox="0 0 16 16"><path d="M1 5c0-2 3-3 7-3s7 1 7 3v1h-4V5H5v1H1z M3 7h10l1 7H2z"/></svg>555 0142 7781</li>
      <li><svg class="icon" viewBox="0 0 16 16"><rect x="4" y="1" width="8" height="14" rx="1.5"/><rect x="5.5" y="3" width="5" height="8" fill="var(--card)"/></svg>555 0198 3364</li>
    </ul>
  </section>

  <section class="card card-back" aria-label="Business card back">
    <div class="brand-block">
      <div class="brand"><span>Fernway Grove</span><span class="brand-dot"></span></div>
      <p class="services">Lawn Mowing <span class="sep">●</span> Garden Maintenance<br>Clean ups &amp; Some Property Maintenance.</p>
    </div>
  </section>
</main>
</body>
</html>
```